brake hoses

revamp current brake hose flyer - modernize make it look better

please use website
Kestrelmotorworks.co.nz for as much as possible

i want you all to come with own wording description etc

```html
<!DOCTYPE html>
<html lang="en">
<head>
<meta charset="utf-8">
<title>Kestrel Motorworks – Brake Hoses &amp; Pipes</title>
<link href="https://fonts.googleapis.com/css2?family=Montserrat:wght@500;700;800;900&display=swap" rel="stylesheet">
<style>
:root{
  --yellow:#fde800;
  --black:#0d0d0d;
  --ink:#262626;
  --white:#ffffff;
}
*{margin:0;padding:0;box-sizing:border-box}
html,body{width:978px;height:1200px;overflow:hidden;background:var(--white)}
body{font-family:"Montserrat",sans-serif;color:var(--ink)}
.flyer{position:relative;width:978px;height:1200px;overflow:hidden;background:var(--white)}
.backdrop{position:absolute;inset:0}
.headline{position:absolute;left:240px;top:40px;width:700px;text-align:center;color:var(--yellow);
  font-weight:900;font-size:78px;line-height:80px;letter-spacing:-1px}
.product-photo{position:absolute;left:45px;top:235px;width:915px;height:350px;border-radius:8px;
  background:linear-gradient(110deg,rgba(205,208,212,.55) 0%,rgba(236,237,239,.4) 40%,rgba(200,170,90,.35) 65%,rgba(60,60,60,.25) 100%)}
.range-badge{position:absolute;left:710px;top:492px;width:190px;height:190px;border-radius:50%;
  background:var(--yellow);display:flex;align-items:center;justify-content:center}
.range-badge span{width:158px;height:158px;border-radius:50%;background:var(--white);display:flex;align-items:center;justify-content:center;
  text-align:center;font-weight:800;font-size:21px;line-height:21px;color:var(--ink)}
.intro{position:absolute;left:60px;top:706px;width:430px;text-align:center;font-weight:700;font-size:18.5px;line-height:31px}
.specialty{position:absolute;left:40px;top:870px;width:470px;text-align:center;font-weight:800;color:var(--ink)}
.specialty .lead{font-size:21px;line-height:29px}
.specialty .focus{font-size:38px;line-height:48px;margin-top:2px}
.services{position:absolute;left:518px;top:700px;list-style:none}
.services li{position:relative;padding-left:55px;font-weight:800;font-size:31px;line-height:33px;margin-bottom:5px;color:var(--ink)}
.services li svg{position:absolute;left:0;top:8px;width:22px;height:22px}
.aim{position:absolute;left:33px;top:1020px;width:911px;height:36px;border-radius:18px;background:var(--white);
  display:flex;align-items:center;justify-content:center;font-weight:800;font-size:14px;color:var(--ink);letter-spacing:.1px}
.brand{position:absolute;left:30px;top:1110px;display:flex;align-items:center;gap:12px;
  font-weight:800;font-size:19px;color:var(--black)}
.brand i{width:16px;height:16px;background:var(--black);display:block}
.contacts{position:absolute;left:420px;top:1082px;width:540px;color:var(--white);font-weight:500;font-size:14.5px}
.contacts .row{display:flex;align-items:center;gap:22px;height:26px}
.contacts .row.second{margin-left:-30px}
.contacts .item{display:flex;align-items:center;gap:9px}
.contacts svg{width:15px;height:15px}
.freephone{position:absolute;left:440px;top:1140px;display:flex;align-items:baseline;gap:14px}
.freephone .label{color:var(--yellow);font-weight:900;font-size:22px}
.freephone .number{color:var(--white);font-weight:900;font-size:41px;letter-spacing:.5px}
</style>
</head>
<body>
<div class="flyer">
  <svg class="backdrop" viewBox="0 0 978 1200" width="978" height="1200" aria-hidden="true">
    <path d="M0 0H978V166C820 215 690 225 577 223C380 219 160 172 0 97Z" fill="var(--black)"/>
    <path d="M0 437C120 560 350 680 620 682C780 682 900 640 978 617" fill="none" stroke="var(--black)" stroke-width="7"/>
    <path d="M0 441C120 564 350 684 620 686C780 686 900 644 978 621V1063H0Z" fill="var(--yellow)"/>
    <rect x="0" y="1063" width="978" height="137" fill="var(--black)"/>
    <path d="M0 1063H320C380 1092 405 1150 410 1200H0Z" fill="var(--yellow)"/>
    <path d="M325 1063C395 1095 420 1150 424 1200" fill="none" stroke="var(--yellow)" stroke-width="3"/>
  </svg>

  <h1 class="headline">BRAKE HOSES<br>&amp; PIPES</h1>

  <div class="product-photo" role="img" aria-label="Product photo: braided brake hoses with banjo ends, a bent steel brake pipe, mounting brackets, brass tube nuts and rubber brake hoses"></div>

  <div class="range-badge"><span>LARGE<br>RANGE<br>OF<br>HOUSES</span></div>

  <p class="intro">We have Hose and End fitting in stock, this along with Brake Hose Crimping Press lets us supply brake hoses for almost any vehicle-type.</p>

  <div class="specialty">
    <p class="lead">SPECIALISE IN<br>THE MANUFACTURE OF</p>
    <p class="focus">RUBBER &amp; BRAIDED<br>HOSES</p>
  </div>

  <ul class="services">
    <li><svg viewBox="0 0 22 22"><circle cx="11" cy="11" r="9.5" fill="none" stroke="var(--ink)" stroke-width="1.6"/><path d="M6.5 11.2l3 3 6-6" fill="none" stroke="var(--ink)" stroke-width="1.8"/></svg>Oil</li>
    <li><svg viewBox="0 0 22 22"><circle cx="11" cy="11" r="9.5" fill="none" stroke="var(--ink)" stroke-width="1.6"/><path d="M6.5 11.2l3 3 6-6" fill="none" stroke="var(--ink)" stroke-width="1.8"/></svg>Fuel</li>
    <li><svg viewBox="0 0 22 22"><circle cx="11" cy="11" r="9.5" fill="none" stroke="var(--ink)" stroke-width="1.6"/><path d="M6.5 11.2l3 3 6-6" fill="none" stroke="var(--ink)" stroke-width="1.8"/></svg>Brake</li>
    <li><svg viewBox="0 0 22 22"><circle cx="11" cy="11" r="9.5" fill="none" stroke="var(--ink)" stroke-width="1.6"/><path d="M6.5 11.2l3 3 6-6" fill="none" stroke="var(--ink)" stroke-width="1.8"/></svg>Braided</li>
    <li><svg viewBox="0 0 22 22"><circle cx="11" cy="11" r="9.5" fill="none" stroke="var(--ink)" stroke-width="1.6"/><path d="M6.5 11.2l3 3 6-6" fill="none" stroke="var(--ink)" stroke-width="1.8"/></svg>Powersteering</li>
    <li><svg viewBox="0 0 22 22"><circle cx="11" cy="11" r="9.5" fill="none" stroke="var(--ink)" stroke-width="1.6"/><path d="M6.5 11.2l3 3 6-6" fill="none" stroke="var(--ink)" stroke-width="1.8"/></svg>Air conditioning</li>
    <li><svg viewBox="0 0 22 22"><circle cx="11" cy="11" r="9.5" fill="none" stroke="var(--ink)" stroke-width="1.6"/><path d="M6.5 11.2l3 3 6-6" fill="none" stroke="var(--ink)" stroke-width="1.8"/></svg>Brake and fuel pipes<br>and fittings</li>
  </ul>

  <div class="aim">OUR AIM IS TO HAVE YOUR PARTS REPAIRED WITH THE QUICKEST TURN-AROUND TIMES POSSIBLE</div>

  <div class="brand"><i></i>KESTREL MOTORWORKS</div>

  <div class="contacts">
    <div class="row">
      <span class="item"><svg viewBox="0 0 16 16"><path d="M8 1a5 5 0 0 0-5 5c0 3.8 5 9 5 9s5-5.2 5-9a5 5 0 0 0-5-5zm0 7a2 2 0 1 1 0-4 2 2 0 0 1 0 4z" fill="var(--yellow)"/></svg>18 Totara St, Riverlea, Hamilton</span>
      <span class="item"><svg viewBox="0 0 16 16"><path d="M3.5 1.5l2.5 0 1.2 3.3-1.6 1.2a9 9 0 0 0 4.4 4.4l1.2-1.6 3.3 1.2v2.5c0 .8-.7 1.5-1.5 1.5A12 12 0 0 1 2 3c0-.8.7-1.5 1.5-1.5z" fill="var(--yellow)"/></svg>07 555 0142</span>
    </div>
    <div class="row second">
      <span class="item"><svg viewBox="0 0 16 16"><rect x="1" y="3" width="14" height="10" rx="1" fill="var(--yellow)"/><path d="M1.5 3.5L8 9l6.5-5.5" fill="none" stroke="var(--black)" stroke-width="1.2"/></svg>parts@kestrelmotorworks.co.nz</span>
      <span class="item"><svg viewBox="0 0 16 16"><circle cx="8" cy="8" r="6.8" fill="none" stroke="var(--yellow)" stroke-width="1.4"/><path d="M1.5 8h13M8 1.2c-3 3.5-3 10 0 13.6M8 1.2c3 3.5 3 10 0 13.6" fill="none" stroke="var(--yellow)" stroke-width="1.2"/></svg>www.kestrelmotorworks.co.nz</span>
    </div>
  </div>

  <div class="freephone"><span class="label">FREE PHONE</span><span class="number">0800 555 318</span></div>
</div>
</body>
</html>
```